Website front page and logo re-designed (using logo provided)

We are looking for the home page of our new website. It is a website offering a space for clients to ask professionals questions. The website should be similar in design to www.quibblenest.com however it is clear it should be a different look. It should be modern, simple to use, a clear navigation bar at the top and bottom.

Logo should be similar to the one attached, but more professional and modern. Logo should be clearly incorporated into website. Design should focus on our website colours as in the logo.

Logo Text

KnowHive - Truth with every reply!

Number of Pages Required

1 page

Font styles to use
Sans Serif

```html
<!DOCTYPE html>
<html lang="en">
<head>
<meta charset="utf-8">
<title>KnowHive – Truth with every reply!</title>
<link rel="stylesheet" href="https://fonts.googleapis.com/css2?family=Roboto:wght@400;500&family=Lato:wght@400;700;900&family=Open+Sans:ital,wght@0,400;0,600;0,700;1,400&display=swap">
<style>
:root{
  --blue:#3a92d8;
  --blue-deep:#2f79b8;
  --blue-row:#3179b9;
  --btn-soft:#6ea6d6;
  --ink:#1d1d1d;
  --black:#050505;
  --band:rgba(28,28,28,.93);
  --grey-text:#7b7b7b;
  --light:#f4f5f5;
  --white:#ffffff;
  --footer-dark:#1f1f1f;
}
*{box-sizing:border-box;margin:0;padding:0}
html,body{width:1200px;height:2299px;overflow:hidden}
body{position:relative;background:var(--white);font-family:"Open Sans",Arial,sans-serif;color:var(--ink)}
.abs{position:absolute}

/* top bar */
.topbar{left:0;top:0;width:1200px;height:43px;background:var(--black)}
.social-dot{top:15px;width:13px;height:13px;border-radius:50%;background:#d9d9d9}
.top-contact{top:12px;font-size:14px;color:#7d8a96;display:flex;align-items:center;gap:8px}
.top-sep{left:826px;top:10px;width:1px;height:22px;background:#333}
.login{left:1065px;top:0;width:87px;height:43px;background:var(--blue);color:#fff;font-size:12px;display:flex;align-items:center;justify-content:center}

/* header */
.header{left:0;top:43px;width:1200px;height:89px;background:var(--light)}
.brand{left:49px;top:56px;display:flex;align-items:center;gap:10px}
.brand-square{width:18px;height:18px;background:var(--blue)}
.brand-name{font-weight:600;font-size:32px;color:var(--blue)}
.nav-active{left:337px;top:37px;width:74px;height:95px;background:var(--blue)}
.nav-item{top:84px;font-size:11.5px;color:#222;text-transform:uppercase;white-space:nowrap}
.nav-item.is-active{color:#fff}
.nav-burger{left:1132px;top:86px;width:18px}
.nav-burger i{display:block;height:2px;background:#333;margin-bottom:2px}

/* hero */
.hero{left:0;top:132px;width:1200px;height:778px;background:linear-gradient(90deg,#d6d6d6 0%,#e9e9e9 35%,#f1f1f1 60%,#e4e4e4 100%)}
.hero-photo{left:600px;top:140px;width:570px;height:770px;background:linear-gradient(180deg,rgba(236,236,236,0) 0%,rgba(214,206,200,.55) 22%,rgba(190,180,172,.5) 40%,#3a3a3d 58%,#1c1c1e 80%,#161618 100%)}
.hero-title{left:49px;top:206px;font-family:"Roboto",sans-serif;font-weight:500;font-size:49px;line-height:63px;color:#222}
.hero-title span{color:var(--blue)}
.hero-copy{left:54px;top:338px;width:612px;font-size:13.5px;line-height:20px;color:#444;letter-spacing:.2px}
.btn-read{left:55px;top:418px;width:149px;height:39px;background:var(--blue);color:#fff;border-radius:3px;font-size:13px;font-weight:600;display:flex;align-items:center;justify-content:center}
.ask-box{left:54px;top:481px;width:508px;height:224px;background:#fff;border:1px solid #d8d8d8}
.ask-placeholder{left:72px;top:508px;font-size:13.5px;color:#c4c4c4}
.ask-foot{left:54px;top:610px;width:508px;height:95px}
.experts-online{left:74px;top:626px;font-family:"Lato",sans-serif;font-size:17px;color:#fff}
.experts-note{left:76px;top:656px;width:270px;font-size:10.5px;line-height:13px;color:#e6f1fb}
.btn-answer{left:355px;top:650px;width:192px;height:41px;background:#2e2e2e;color:#fff;border-radius:3px;font-family:"Lato",sans-serif;font-size:19px;display:flex;align-items:center;justify-content:center}
.slide-dot{top:699px;width:23px;height:4px}

/* feature band */
.features{left:0;top:705px;width:1200px;height:205px;background:var(--band)}
.feature{top:726px;width:260px;text-align:center}
.feature-icon{margin:0 auto;width:78px;height:78px;border-radius:50%;display:flex;align-items:center;justify-content:center}
.feature-title{margin-top:15px;font-family:"Lato",sans-serif;font-weight:700;font-size:14.5px;letter-spacing:.5px;color:var(--blue);text-transform:uppercase}
.feature-text{margin-top:2px;font-size:11.5px;line-height:15px;color:#e8e8e8}
.feature-next{top:888px;width:48px;height:48px;border-radius:50%;background:#fff;border:2px solid var(--blue);display:flex;align-items:center;justify-content:center}
.feature-next.is-current{background:var(--blue)}

/* experts */
.expert-avatar{top:1003px;width:76px;height:76px;border-radius:50%;border:2px solid var(--blue);padding:4px;background:#fff}
.expert-avatar div{width:100%;height:100%;border-radius:50%;background:linear-gradient(180deg,#c9c9c9,#8a94a0)}
.expert-name{top:993px;font-family:"Lato",sans-serif;font-weight:700;font-size:27px;color:#111;white-space:nowrap}
.expert-name span{color:var(--blue)}
.expert-name small{font-weight:400;font-size:13px;color:#444}
.expert-text{top:1031px;width:235px;font-size:12px;line-height:23px;color:#888}
.carousel-arrow{top:1024px}

/* questions */
.questions{left:0;top:1183px;width:1200px;height:449px;background:var(--blue)}
.section-title{width:1200px;left:0;text-align:center;font-family:"Roboto",sans-serif;font-weight:500;font-size:34px;letter-spacing:.5px;color:#111}
.section-title .on-blue{color:#fff}
.section-title .accent{color:var(--blue)}
.recent-label{left:112px;top:1295px;font-family:"Lato",sans-serif;font-size:17px;color:#fff}
.view-all{left:1041px;top:1304px;font-size:11.5px;color:#fff}
.q-row{left:110px;width:981px;height:77px;background:var(--blue-row)}
.q-text{left:36px;top:28px;font-family:"Lato",sans-serif;font-weight:700;font-size:14.5px;color:#fff;display:flex;align-items:center;gap:12px}
.q-divider{top:15px;width:1px;height:47px;background:#5ba1dc}
.q-rating{left:659px;top:16px;width:80px;text-align:center;font-size:12px;color:#fff}
.stars{margin-top:5px;letter-spacing:2px;font-size:13px}
.q-btn{left:791px;top:21px;width:172px;height:37px;background:var(--btn-soft);color:#fff;font-size:11.5px;display:flex;align-items:center;justify-content:center}

/* testimonials */
.quote-box{left:336px;top:1767px;width:400px;height:169px;border:1px solid #e4e4e4;background:#fff}
.quote-text{left:358px;top:1810px;width:360px;font-style:italic;font-size:12px;line-height:22.5px;color:#888}
.testi-avatar{left:776px;top:1767px;width:83px;height:83px;border-radius:50%;border:2px solid #333;padding:4px;background:#fff}
.testi-avatar div{width:100%;height:100%;border-radius:50%;background:linear-gradient(180deg,#d6d6d6,#7f8c97)}
.testi-name{left:760px;top:1855px;width:115px;text-align:center;font-weight:600;font-size:19px;color:var(--blue)}
.testi-loc{left:780px;top:1884px;font-size:11px;color:#888}

/* footer */
.footer{left:0;top:2005px;width:1200px;height:214px;background:linear-gradient(180deg,#3a92d8,#3687cb)}
.foot-head{top:2035px;font-weight:700;font-size:16.5px;color:#fff;text-transform:uppercase}
.foot-links{left:50px;top:2070px;list-style:none}
.foot-links li{height:28.5px;font-size:11.5px;color:#eaf4fd;display:flex;align-items:center;gap:8px}
.foot-links li::before{content:"";width:11px;height:11px;border-radius:50%;border:1px solid #bcdcf5}
.field{height:40px;border:1px solid #cfe5f7;color:#cfe5f7;font-size:11.5px;font-style:italic;padding:12px 10px}
.submit{left:259px;top:2166px;width:130px;height:36px;background:#555;color:#fff;font-size:14px;display:flex;align-items:center;justify-content:center}
.foot-info{left:657px;top:2077px;font-size:11.5px;line-height:27px;color:#fff}
.follow-dot{top:2094px;width:34px;height:34px;border-radius:50%;background:#fff}
.copybar{left:0;top:2219px;width:1200px;height:80px;background:var(--footer-dark)}
.copy{left:75px;top:2250px;font-size:11.5px;color:#fff}
</style>
</head>
<body>

<!-- top bar -->
<div class="abs topbar"></div>
<div class="abs social-dot" style="left:47px"></div>
<div class="abs social-dot" style="left:87px"></div>
<div class="abs social-dot" style="left:125px"></div>
<div class="abs social-dot" style="left:161px"></div>
<div class="abs social-dot" style="left:199px"></div>
<div class="abs top-contact" style="left:686px">
  <svg width="16" height="16" viewBox="0 0 16 16"><path d="M4 1l3 3-2 2c1 2 3 4 5 5l2-2 3 3-2 3C7 15 1 9 1 3z" fill="#3a92d8"/></svg>1432-765-980</div>
<div class="abs top-sep"></div>
<div class="abs top-contact" style="left:850px">
  <svg width="16" height="12" viewBox="0 0 16 12"><rect x="1" y="1" width="14" height="10" fill="none" stroke="#3a92d8" stroke-width="1.5"/><path d="M1 1l7 6 7-6" fill="none" stroke="#3a92d8" stroke-width="1.5"/></svg>hello@knowhive.com</div>
<div class="abs login">LOGIN</div>

<!-- header -->
<header class="abs header"></header>
<div class="abs brand"><span class="brand-square"></span><span class="brand-name">KnowHive</span></div>
<div class="abs nav-active"></div>
<nav>
  <span class="abs nav-item is-active" style="left:348px">Lawyers</span>
  <span class="abs nav-item" style="left:443px">Mechanics</span>
  <span class="abs nav-item" style="left:553px">Doctors &amp; Nurses</span>
  <span class="abs nav-item" style="left:707px">Vets</span>
  <span class="abs nav-item" style="left:779px">Electricians &amp; Plumbers</span>
  <span class="abs nav-item" style="left:972px">Computer &amp; Education</span>
  <span class="abs nav-burger"><i></i><i></i><i></i></span>
</nav>

<!-- hero -->
<section class="abs hero"></section>
<div class="abs hero-photo" role="img" aria-label="Photo of a smiling professional in a dark suit with arms crossed"></div>
<h1 class="abs hero-title">Know Your Answer <span>QUICKLE</span><br>For Your Question</h1>
<p class="abs hero-copy">Lorem ipsum dolor sit amet, consectetur adipiscing elit, sed do eiusmod tempor incidi-dunt ut labore et dolore magna aliqua. Ut enim ad minim veniam, quis nostrud exercita-tion ullamco laboris nisi ut aliquip ex ea commodo consequat.</p>
<div class="abs btn-read">READ MORE</div>
<div class="abs ask-box"></div>
<div class="abs ask-placeholder">Choose an Expert and type your question here....</div>
<svg class="abs ask-foot" viewBox="0 0 508 95" style="overflow:visible"><path d="M0 0H418L447 -30V0H508V95H0Z" fill="#3a92d8"/></svg>
<div class="abs experts-online">52 Experts are Online Now</div>
<div class="abs experts-note">Lorem ipsum dolor sit amet, consectetur adipisc-ing elit, sed do eiusmod tempor</div>
<div class="abs btn-answer">Get an Answer</div>
<div class="abs slide-dot" style="left:1023px;background:#3ab6d8"></div>
<div class="abs slide-dot" style="left:1055px;background:#e8b83a"></div>
<div class="abs slide-dot" style="left:1087px;background:#3ab6d8"></div>

<!-- features -->
<div class="abs features"></div>
<div class="abs feature" style="left:40px">
  <div class="feature-icon" style="background:var(--blue)"><svg width="38" height="38" viewBox="0 0 24 24"><path d="M2 10h4v11H2zM8 10l5-8c2 0 3 1 2.5 3L14 9h6c1.5 0 2.5 1.5 2 3l-2 7c-.4 1.2-1.3 2-2.5 2H8z" fill="#fff"/></svg></div>
  <div class="feature-title">Convenience</div>
  <div class="feature-text">Lorem ipsum dolor sit amet, consectetur<br>adipiscing elit, sed do eiusmod tempor<br>incididunt ut labore</div>
</div>
<div class="abs feature" style="left:334px">
  <div class="feature-icon" style="background:#fff"><svg width="36" height="36" viewBox="0 0 24 24"><circle cx="12" cy="7" r="5" fill="#3a92d8"/><path d="M3 22c0-6 4-9 9-9s9 3 9 9z" fill="#3a92d8"/></svg></div>
  <div class="feature-title">One on One</div>
  <div class="feature-text">Lorem ipsum dolor sit amet, consectetur<br>adipiscing elit, sed do eiusmod tempor<br>incididunt ut labore</div>
</div>
<div class="abs feature" style="left:636px">
  <div class="feature-icon" style="background:#fff"><svg width="38" height="38" viewBox="0 0 24 24"><circle cx="12" cy="12" r="10" fill="#3a92d8"/><circle cx="12" cy="12" r="7.5" fill="#fff"/><path d="M12 7v5h4" stroke="#3a92d8" stroke-width="2" fill="none"/></svg></div>
  <div class="feature-title">24/7 Availability</div>
  <div class="feature-text">Lorem ipsum dolor sit amet, consectetur<br>adipiscing elit, sed do eiusmod tempor<br>incididunt ut labore</div>
</div>
<div class="abs feature" style="left:912px">
  <div class="feature-icon" style="background:#fff"><svg width="38" height="38" viewBox="0 0 24 24"><path d="M2 10h4v11H2zM8 10l5-8c2 0 3 1 2.5 3L14 9h6c1.5 0 2.5 1.5 2 3l-2 7c-.4 1.2-1.3 2-2.5 2H8z" fill="#3a92d8"/></svg></div>
  <div class="feature-title">100% Satisfaction</div>
  <div class="feature-text">Lorem ipsum dolor sit amet, consectetur<br>adipiscing elit, sed do eiusmod tempor<br>incididunt ut labore</div>
</div>
<div class="abs feature-next is-current" style="left:142px"><svg width="14" height="14" viewBox="0 0 14 14"><path d="M5 2l5 5-5 5" stroke="#fff" stroke-width="2.4" fill="none"/></svg></div>
<div class="abs feature-next" style="left:438px"><svg width="14" height="14" viewBox="0 0 14 14"><path d="M5 2l5 5-5 5" stroke="#3a92d8" stroke-width="2.4" fill="none"/></svg></div>
<div class="abs feature-next" style="left:739px"><svg width="14" height="14" viewBox="0 0 14 14"><path d="M5 2l5 5-5 5" stroke="#3a92d8" stroke-width="2.4" fill="none"/></svg></div>
<div class="abs feature-next" style="left:1017px"><svg width="14" height="14" viewBox="0 0 14 14"><path d="M5 2l5 5-5 5" stroke="#3a92d8" stroke-width="2.4" fill="none"/></svg></div>

<!-- experts -->
<svg class="abs carousel-arrow" style="left:30px" width="18" height="24" viewBox="0 0 18 24"><path d="M16 2L2 12l14 10z" fill="#dcdcdc"/></svg>
<svg class="abs carousel-arrow" style="left:1152px" width="18" height="24" viewBox="0 0 18 24"><path d="M2 2l14 10L2 22z" fill="#dcdcdc"/></svg>

<div class="abs expert-avatar" style="left:72px"><div role="img" aria-label="Expert portrait"></div></div>
<div class="abs expert-name" style="left:161px">Aaron <span>Pell,</span> <small>Software</small></div>
<p class="abs expert-text" style="left:161px">Lorem ipsum dolor sit amet, consectetur adipiscing elit, sed do eiusmod editsincidi-dunt ut labore et dolore tempor.</p>

<div class="abs expert-avatar" style="left:441px"><div role="img" aria-label="Expert portrait"></div></div>
<div class="abs expert-name" style="left:530px">Marcus <span>Reed,</span> <small>Doctor</small></div>
<p class="abs expert-text" style="left:532px">Lorem ipsum dolor sit amet, consectetur adipiscing elit, sed do eiusmod editsincidi-dunt ut labore et dolore tempor.</p>

<div class="abs expert-avatar" style="left:806px"><div role="img" aria-label="Expert portrait"></div></div>
<div class="abs expert-name" style="left:895px">Owen <span>Harte,</span> <small>Lawyer</small></div>
<p class="abs expert-text" style="left:897px">Lorem ipsum dolor sit amet, consectetur adipiscing elit, sed do eiusmod editsincidi-dunt ut labore et dolore tempor.</p>

<!-- recently answered -->
<section class="abs questions"></section>
<h2 class="abs section-title" style="top:1227px">JOIN THE <span class="on-blue">MANY PEOPLES</span></h2>
<div class="abs recent-label">Recently Answered Questions</div>
<div class="abs view-all">View All</div>

<div class="abs q-row" style="top:1326px">
  <div class="abs q-text"><svg width="16" height="16" viewBox="0 0 16 16"><path d="M15 1L1 7l5 2 1 6 2-4 4 2z" fill="#fff"/></svg>If using a syringe to wet a patients mouth who is on terminal</div>
  <div class="abs q-divider" style="left:635px"></div>
  <div class="abs q-rating">RATING<div class="stars">★★★★★</div></div>
  <div class="abs q-divider" style="left:759px"></div>
  <div class="abs q-btn">READ MORE</div>
</div>
<div class="abs q-row" style="top:1424px">
  <div class="abs q-text"><svg width="16" height="16" viewBox="0 0 16 16"><path d="M15 1L1 7l5 2 1 6 2-4 4 2z" fill="#fff"/></svg>If using a syringe to wet a patients mouth who is on terminal</div>
  <div class="abs q-divider" style="left:635px"></div>
  <div class="abs q-rating">RATING<div class="stars">★★★★★</div></div>
  <div class="abs q-divider" style="left:759px"></div>
  <div class="abs q-btn">READ MORE</div>
</div>
<div class="abs q-row" style="top:1523px">
  <div class="abs q-text"><svg width="16" height="16" viewBox="0 0 16 16"><path d="M15 1L1 7l5 2 1 6 2-4 4 2z" fill="#fff"/></svg>If using a syringe to wet a patients mouth who is on terminal</div>
  <div class="abs q-divider" style="left:635px"></div>
  <div class="abs q-rating">RATING<div class="stars">★★★★★</div></div>
  <div class="abs q-divider" style="left:759px"></div>
  <div class="abs q-btn">READ MORE</div>
</div>

<!-- testimonials -->
<h2 class="abs section-title" style="top:1670px">OUR <span class="accent">TESTIMONIALS</span></h2>
<svg class="abs" style="left:167px;top:1793px" width="42" height="108" viewBox="0 0 42 108"><path d="M40 2L3 54l37 52" stroke="#c8c8c8" stroke-width="2" fill="none"/></svg>
<svg class="abs" style="left:973px;top:1793px" width="42" height="108" viewBox="0 0 42 108"><path d="M2 2l37 52L2 106" stroke="#c8c8c8" stroke-width="2" fill="none"/></svg>
<div class="abs quote-box"></div>
<svg class="abs" style="left:734px;top:1800px" width="28" height="40" viewBox="0 0 28 40"><path d="M0 0L26 20 0 38" fill="#fff" stroke="#e4e4e4"/><rect x="0" y="1" width="2" height="36" fill="#fff"/></svg>
<svg class="abs" style="left:328px;top:1752px" width="44" height="36" viewBox="0 0 44 36"><path d="M2 34V20C2 8 8 3 18 2v6c-5 1-7 4-7 8h7v18zM24 34V20c0-12 6-17 16-18v6c-5 1-7 4-7 8h7v18z" fill="#d5d5d5"/></svg>
<svg class="abs" style="left:694px;top:1912px" width="44" height="36" viewBox="0 0 44 36"><path d="M42 2v14c0 12-6 17-16 18v-6c5-1 7-4 7-8h-7V2zM20 2v14c0 12-6 17-16 18v-6c5-1 7-4 7-8H4V2z" fill="#d5d5d5"/></svg>
<p class="abs quote-text">Lorem ipsum dolor sit amet, consectetur adipiscing elit, sed do eiusmod tempor incididunt ut labore et dolore magna aliqua. Ut enim ad minim veniam, quis nostrud exercitation ullamco laboris nisi ut aliquip ex ea commodo consequat.</p>
<div class="abs testi-avatar"><div role="img" aria-label="Client portrait"></div></div>
<div class="abs testi-name">Aaron Pell</div>
<div class="abs testi-loc">City&nbsp;&nbsp;Location</div>

<!-- footer -->
<footer class="abs footer" role="img" aria-label="Faint world map behind footer content"></footer>
<div class="abs foot-head" style="left:50px">About Us</div>
<ul class="abs foot-links">
  <li>Home</li><li>Browse Activities</li><li>The Market</li><li>How it works</li><li>Blog</li>
</ul>
<div class="abs foot-head" style="left:253px">Contact Us</div>
<div class="abs field" style="left:257px;top:2074px;width:157px">Name</div>
<div class="abs field" style="left:418px;top:2074px;width:157px">Phone</div>
<div class="abs field" style="left:257px;top:2118px;width:157px">E-mail</div>
<div class="abs field" style="left:418px;top:2118px;width:157px">Message</div>
<div class="abs submit">SUBMIT</div>
<div class="abs foot-head" style="left:654px">Have Questions?</div>
<div class="abs foot-info">321-654-0987<br>hello@knowhive.com<br>Lorem Ipsum is simply dummy</div>
<div class="abs foot-head" style="left:947px">Follow Us</div>
<div class="abs follow-dot" style="left:944px"></div>
<div class="abs follow-dot" style="left:988px"></div>
<div class="abs follow-dot" style="left:1034px"></div>
<div class="abs follow-dot" style="left:1080px"></div>
<div class="abs copybar"></div>
<div class="abs copy">Copy Right @ 2015 KnowHive.All Rights Reserved</div>

</body>
</html>
```